Brio 41 specialty coffee shop business card

Please use Design #5812047 from previous project (logo design). Brio 41 is a new coffee shop that will serve specialty coffee and will focus on high quality products. I would like to use orange and brown colors. I like designs that are simple but elegant and that deliver a message that is easy to recognize. I will upload a file of the logo design.

Industry/Entity Type

Coffee Shop

Contact Information for Business Card

Leon Cordravik
(555) 203-7719

Font styles to use
Serif
Sans Serif
Script

Requirements
Must have
• simple and elegant, colors match nicely, I like to use orange and brown. Background creme color.
Should not have
• complex designs that are hard to understand.

```html
<!DOCTYPE html>
<html lang="en">
<head>
<meta charset="utf-8">
<title>Brio 41 – Business Card</title>
<link rel="stylesheet" href="https://fonts.googleapis.com/css2?family=Raleway:wght@500;600&display=swap">
<style>
  :root {
    --backdrop: #e9e7e4;
    --cream: #fdd2b3;
    --orange: #f15a22;
    --orange-back: #f26524;
    --brown: #8a5534;
    --brown-dark: #4a2c1a;
    --card-shadow: rgba(40, 30, 20, 0.22);
  }
  * { margin: 0; padding: 0; box-sizing: border-box; }
  html, body {
    width: 1200px;
    height: 873px;
    overflow: hidden;
    background: var(--backdrop);
    font-family: "Raleway", sans-serif;
  }
  .stage {
    width: 1200px;
    height: 873px;
    display: flex;
    align-items: center;
    justify-content: center;
    gap: 40px;
  }
  .card {
    position: relative;
    width: 540px;
    height: 309px;
    border-radius: 4px;
    overflow: hidden;
    box-shadow: 0 10px 28px var(--card-shadow);
  }
  .card--front { background: var(--cream); }
  .card--back { background: var(--orange-back); }
  .card__waves {
    position: absolute;
    inset: 0;
    width: 100%;
    height: 100%;
  }
  .wave--orange { fill: var(--orange); }
  .wave--brown { fill: var(--brown); }

  .brand {
    position: absolute;
    left: 170px;
    top: 95px;
    display: flex;
    align-items: center;
    gap: 12px;
    color: var(--brown-dark);
  }
  .brand__dot {
    width: 22px;
    height: 22px;
    border-radius: 50%;
    background: var(--brown);
  }
  .brand__name {
    font-size: 46px;
    font-weight: 600;
    letter-spacing: 1px;
  }

  .contact {
    position: absolute;
    left: 28px;
    top: 232px;
    list-style: none;
    color: var(--cream);
    font-size: 11px;
    font-weight: 500;
    letter-spacing: 0.3px;
  }
  .contact__item {
    display: flex;
    align-items: center;
    gap: 8px;
    line-height: 19px;
  }
  .contact__mark {
    width: 10px;
    height: 10px;
    border-radius: 50%;
    background: var(--cream);
    flex: none;
  }
  .contact__icon {
    width: 10px;
    height: 10px;
    flex: none;
  }
</style>
</head>
<body>
  <main class="stage">
    <section class="card card--front" aria-label="Business card front">
      <svg class="card__waves" viewBox="0 0 540 309" preserveAspectRatio="none" aria-hidden="true">
        <path class="wave--orange" d="M0,178 C110,214 270,236 370,232 C460,226 512,130 540,56 L540,309 L0,309 Z"/>
        <path class="wave--brown" d="M250,236 C360,240 470,214 540,38 L540,96 C500,196 440,244 370,248 C330,250 290,244 250,236 Z"/>
      </svg>

      <div class="brand">
        <span class="brand__dot"></span>
        <span class="brand__name">Brio 41</span>
      </div>

      <ul class="contact">
        <li class="contact__item"><span class="contact__mark"></span>brio41cafe.com/news</li>
        <li class="contact__item"><span class="contact__mark"></span>brio41cafe.com/chat</li>
        <li class="contact__item">
          <svg class="contact__icon" viewBox="0 0 24 24" aria-hidden="true">
            <path fill="#fdd2b3" d="M6.6 10.8a15.2 15.2 0 0 0 6.6 6.6l2.2-2.2a1 1 0 0 1 1-.25 11.4 11.4 0 0 0 3.6.57 1 1 0 0 1 1 1V20a1 1 0 0 1-1 1A17 17 0 0 1 3 4a1 1 0 0 1 1-1h3.5a1 1 0 0 1 1 1c0 1.25.2 2.45.57 3.57a1 1 0 0 1-.25 1z"/>
          </svg>
          (555) 203-7719
        </li>
      </ul>
    </section>

    <section class="card card--back" aria-label="Business card back"></section>
  </main>
</body>
</html>
```